Upscale business cards needed for family office

We would like professional business cards created for employees of our family office. Relatively simple and straightforward, but also with a unique element to set them apart. Probably stick with neutral and simple colors that mesh well with the colors in the logo. We need space for the traditional elements, including name, title, address, email/phone number.

Industry/Entity Type

Business

Contact Information for Business Card

Space for name, title, phone number, email, address

```html
<!DOCTYPE html>
<html lang="en">
<head>
<meta charset="utf-8">
<title>H&amp;R Business Card</title>
<link href="https://fonts.googleapis.com/css2?family=Montserrat:wght@400;500;600;700&display=swap" rel="stylesheet">
<style>
  :root {
    --backdrop: #e6e7e8;
    --card: #ffffff;
    --band-grey: #a3a5a8;
    --band-grey-dark: #8d8f92;
    --accent-blue: #2aa3c9;
    --ink: #5f6266;
    --ink-soft: #8a8d91;
    --white: #ffffff;
  }
  * { box-sizing: border-box; margin: 0; padding: 0; }
  html, body {
    width: 1200px; height: 900px; overflow: hidden;
    background: var(--backdrop);
    font-family: "Montserrat", Arial, sans-serif;
  }
  .stage {
    width: 1200px; height: 900px;
    display: flex; align-items: center; justify-content: center;
  }
  .business-card {
    position: relative;
    width: 840px; height: 480px;
    background: var(--card);
    overflow: hidden;
    box-shadow: 0 6px 24px rgba(0,0,0,0.12);
  }
  .grey-band {
    position: absolute; top: 0; right: 0;
    width: 560px; height: 230px;
    background: linear-gradient(180deg, var(--band-grey) 0%, var(--band-grey-dark) 100%);
    border-bottom-left-radius: 46px;
  }
  .name-tab {
    position: absolute; right: 0; top: 150px;
    width: 430px; height: 96px;
    background: var(--accent-blue);
    border-top-left-radius: 30px;
    border-bottom-left-radius: 30px;
    padding: 18px 0 0 34px;
    color: var(--white);
  }
  .name-tab .person-name {
    font-size: 30px; font-weight: 600; letter-spacing: 1.5px;
  }
  .name-tab .person-title {
    font-size: 16px; font-weight: 500; letter-spacing: 3px; margin-top: 4px;
  }
  .brand {
    position: absolute; left: 64px; top: 70px;
    display: flex; align-items: center; gap: 14px;
  }
  .brand-square {
    width: 22px; height: 22px; background: var(--accent-blue);
  }
  .brand-name {
    font-size: 46px; font-weight: 600; color: var(--ink); letter-spacing: 1px;
  }
  .contact {
    position: absolute; left: 64px; top: 300px;
    font-size: 15px; color: var(--ink); letter-spacing: 1.5px;
    line-height: 28px;
  }
  .contact .label {
    display: inline-block; width: 96px; color: var(--accent-blue); font-weight: 600;
  }
  .address {
    position: absolute; left: 64px; top: 384px;
    font-size: 13px; color: var(--ink-soft); letter-spacing: 1.4px;
  }
  .website {
    position: absolute; right: 60px; top: 420px;
    font-size: 14px; color: var(--ink-soft); letter-spacing: 2.5px;
  }
</style>
</head>
<body>
<main class="stage">
  <article class="business-card">
    <div class="grey-band"></div>
    <div class="name-tab">
      <div class="person-name">NAME SURNAME</div>
      <div class="person-title">TITLE</div>
    </div>
    <div class="brand">
      <span class="brand-square"></span>
      <span class="brand-name">H&amp;R</span>
    </div>
    <div class="contact">
      <div><span class="label">PHONE:</span>+000 00 00 000</div>
      <div><span class="label">E-MAIL:</span>NAME.SURNAME@HRFAMILY.COM</div>
    </div>
    <div class="address">MAIN ROAD, SOME STREET NO 5, SOME DISTRICT, DOWNTOWN, COUNTRY</div>
    <div class="website">WWW.HRFAMILY.COM</div>
  </article>
</main>
</body>
</html>
```